Design profile for MuroDeck Nordhaven

I had a logo competition here recently, and was left with two logos that I could not choose between. Therefore, I create this competition where I want a complete design package or a visual identity for the company. I want you to create design elements that can be used both in print and online. (letterhead, envelopes, business card, website, facebook, etc.) I have also attached a picture of the car I have ordered. I'm happy if you can show how the design can be used on that as well.
What is important is that the logos are treated individually, and that the design you create reflects or builds up under the logo. I want the design to be recognizable and to have a connection with the logo and what we do. (take fizzo lumo as an example. if you remove the name, but keep the red color and the white line, then you will recognize which brand it is about right away)
You choose whether you want to make proposals only for one logo, or or both, but it is important that they are treated individually. The best overall package determines which logo I use.
I have also added an image that you can use as an example background if you want it in a facebook banner for example.
It is important that the design looks professional and unique. A number of designs have come in, but many of the designs are very similar and general. Here is a video of the printer if you need inspiration: https://clipvault.example/v/Q8ZtrMx2LwK

Industry/Entity Type

WallPrinting

Requirements
Must have
• Unique an professional design that can be used both online and print
Nice to have
• Show how to use the design on a VX Tully. (see photos attached)
Should not have
• The design can be simple, but not too simple and general. I want it to give the company an identity

```html
<!DOCTYPE html>
<html lang="en">
<head>
<meta charset="utf-8">
<title>MuroDeck Nordhaven – Company Profile 2022</title>
<link href="https://fonts.googleapis.com/css2?family=Montserrat:wght@400;500;600;700;800&display=swap" rel="stylesheet">
<style>
:root{
  --teal:#2eafc6;
  --teal-dark:#1f93a8;
  --ink:#2f2f2f;
  --grey:#555;
  --magenta:#e4197c;
  --yellow:#f2c318;
  --paper:#ffffff;
  --stage:#d9cdd2;
}
*{margin:0;padding:0;box-sizing:border-box}
html,body{width:1200px;height:811px;overflow:hidden}
body{background:linear-gradient(135deg,#d3c3c9,#dedade 60%,#e3e3e5);font-family:'Montserrat',sans-serif;color:var(--ink)}
.spread{position:absolute;left:0;top:0;width:1500px;height:1014px;transform:scale(.8);transform-origin:0 0}
.page{position:absolute;width:335px;height:474px;background:var(--paper);overflow:hidden;box-shadow:2px 3px 6px rgba(0,0,0,.35)}
.abs{position:absolute}
.lorem{font-size:5.6px;line-height:8.4px;color:var(--grey)}
.lorem.light{color:#fff}
.lorem p+p{margin-top:8px}
.heading{font-weight:700;font-size:15px;letter-spacing:.3px;color:var(--ink)}
.heading.light{color:#fff}
.wordmark{position:absolute;font-weight:600;color:var(--ink);line-height:1}
.wordmark .name{display:block;font-size:15px;letter-spacing:-.2px}
.wordmark .place{display:block;font-size:4.5px;letter-spacing:1px;text-align:center;margin-top:1px}
.wordmark.light{color:#fff}
.folio{position:absolute;right:12px;bottom:40px;font-size:4.5px;color:#777}
.hex{position:absolute}
.hex svg{display:block;width:100%;height:100%}
/* contents */
.toc-row{position:absolute;left:19px;width:250px;font-size:6px;display:flex;align-items:center}
.toc-row .no{width:40px}
.toc-row .dots{flex:1;border-bottom:1px dotted currentColor;margin:0 8px;height:0}
.toc-row .pg{width:10px}
.num{position:absolute;left:19px;width:19px;height:19px;border-radius:50%;background:var(--teal);color:#fff;font-size:6px;font-weight:600;display:flex;align-items:center;justify-content:center}
.num-text{position:absolute;left:49px;width:120px;font-size:5.6px;line-height:8px;color:var(--grey)}
.member-name{font-size:6.5px;font-weight:700;color:var(--ink)}
.member-role{font-size:5.5px;color:var(--ink);margin-top:2px;padding-bottom:5px;border-bottom:1px solid var(--teal);width:75px}
.contact-line{display:flex;gap:9px;font-size:6px;line-height:8px;color:var(--ink);margin-bottom:8px}
.contact-line svg{width:8px;height:8px;flex:none;margin-top:1px}
</style>
</head>
<body>
<div class="spread">

<!-- Cover -->
<section class="page" style="left:36px;top:24px;background:var(--teal)">
  <div class="wordmark light" style="left:23px;top:58px"><span class="name" style="font-size:17px">MuroDeck</span><span class="place">NORDHAVEN</span></div>
  <div class="abs heading light" style="left:23px;top:80px;font-size:22px;line-height:26px;font-weight:800">PROFILE<br>2022</div>
  <div class="abs" style="left:167px;top:38px;width:168px;height:398px;background:#fff"></div>
  <div class="wordmark" style="left:190px;top:62px"><span class="name">MuroDeck</span><span class="place">NORDHAVEN</span></div>
  <div class="abs lorem" style="left:190px;top:84px;width:125px">Lorem Ipsum is simply dummy text of the printing and typesetting industry.</div>
  <div class="hex" style="left:58px;top:118px;width:212px;height:240px" role="img" aria-label="Large format printer head laying colour onto media">
    <svg viewBox="0 0 100 100" preserveAspectRatio="none">
      <defs><linearGradient id="coverImg" x1="0" y1="0" x2="1" y2="1"><stop offset="0" stop-color="#3a3a3a"/><stop offset=".4" stop-color="#c9302c"/><stop offset=".65" stop-color="#f3a21c"/><stop offset="1" stop-color="#6fb3c9"/></linearGradient></defs>
      <polygon points="50,0 100,25 100,75 50,100 0,75 0,25" fill="#fff"/>
      <polygon points="50,4 96,27 96,73 50,96 4,73 4,27" fill="url(#coverImg)"/>
    </svg>
  </div>
  <div class="abs lorem" style="left:190px;top:398px;width:130px;padding-bottom:5px;border-bottom:1px solid var(--teal)">Lorem Ipsum is simply dummy text of the printing and typesetting industry.</div>
</section>

<!-- Table of contents -->
<section class="page" style="left:401px;top:24px">
  <div class="abs" style="left:0;top:0;width:335px;height:44px;background:var(--teal)"></div>
  <div class="abs" style="left:304px;top:0;width:31px;height:324px;background:var(--teal)"></div>
  <div class="abs heading light" style="left:82px;top:14px;font-size:13.5px;padding-bottom:2px;border-bottom:2px solid #fff">TABLE OF CONTENTS</div>
  <div class="toc-row" style="top:85px;color:var(--teal);font-weight:600;font-size:6.5px"><span class="no" style="border-bottom:1px solid var(--teal);width:26px;margin-right:14px">SL NO</span><span style="border-bottom:1px solid var(--teal)">DESCRIPTION</span><span style="flex:1"></span><span style="border-bottom:1px solid var(--teal)">PAGE NUMBER</span></div>
  <div class="toc-row" style="top:114px;color:var(--teal)"><span class="no">01</span><span>Introduction</span><span class="dots"></span><span class="pg">02</span></div>
  <div class="toc-row" style="top:144px;color:var(--magenta)"><span class="no">02</span><span>Vision</span><span class="dots"></span><span class="pg">03</span></div>
  <div class="toc-row" style="top:174px;color:var(--yellow)"><span class="no">03</span><span>Mission</span><span class="dots"></span><span class="pg">04</span></div>
  <div class="toc-row" style="top:205px;color:var(--ink)"><span class="no">04</span><span>Our Best Services</span><span class="dots"></span><span class="pg">05</span></div>
  <div class="toc-row" style="top:235px;color:var(--teal)"><span class="no">05</span><span>Our Team</span><span class="dots"></span><span class="pg">05</span></div>
  <div class="toc-row" style="top:265px;color:var(--magenta)"><span class="no">06</span><span>Contact Us</span><span class="dots"></span><span class="pg">05</span></div>
  <div class="abs" style="left:0;top:330px;width:335px;height:144px;background:linear-gradient(170deg,#ffffff 0%,#e9e3ee 20%,#c9a6cf 38%,#9fd3d0 52%,#e7a6c4 66%,#b7c87e 80%,#8fa6d6 100%)" role="img" aria-label="Printed wallpaper roll with colourful stripes"></div>
  <span class="folio" style="bottom:50px">02</span>
</section>

<!-- Introduction -->
<section class="page" style="left:767px;top:24px">
  <div class="abs" style="left:0;top:0;width:145px;height:324px;background:var(--teal)"></div>
  <div class="abs" style="left:25px;top:31px;width:120px;height:263px;background:linear-gradient(160deg,#f4f4f4 0%,#7fd0e6 25%,#e54d9a 45%,#f5d43a 62%,#8bc34a 78%,#ffffff 100%)" role="img" aria-label="Ink brush sweeping rainbow colour stripes"></div>
  <div class="abs heading" style="left:188px;top:15px;font-size:13.5px;padding-bottom:2px;border-bottom:2px solid var(--teal)">INTRODUCTION</div>
  <div class="abs lorem" style="left:178px;top:40px;width:145px">
    <p>Lorem Ipsum is simply dummy text of the printing and typesetting industry. Ut wisi enim ad minim veniam, quis nostrud exerci tation ullamcorper suscipit lobortis nisl ut aliquip ex ea commodo consequat. Duis autem vel eum iriure dolor in hendrerit in vulputate velit esse molestie consequat.</p>
    <p>Lorem Ipsum is simply dummy text of the printing and typesetting industry. Ut wisi enim ad minim veniam, quis nostrud exerci tation ullamcorper suscipit lobortis nisl ut aliquip ex ea commodo consequat.</p>
    <p>Lorem Ipsum is simply dummy text of the printing and typesetting industry. Ut wisi enim ad minim veniam, quis nostrud exerci tation ullamcorper suscipit lobortis nisl ut aliquip ex ea commodo consequat. Duis autem vel eum iriure dolor in hendrerit in vulputate velit esse molestie consequat.</p>
    <p>Lorem Ipsum is simply dummy text of the printing and typesetting industry. Ut wisi enim ad minim veniam, quis nostrud exerci tation ullamcorper suscipit lobortis nisl ut aliquip ex ea commodo consequat. Duis autem vel eum iriure dolor in hendrerit in vulputate velit esse molestie consequat. Lorem Ipsum is simply dummy text of the printing and typesetting industry.</p>
  </div>
  <div class="abs lorem" style="left:25px;top:346px;width:295px">Lorem Ipsum is simply dummy text of the printing and typesetting industry. Lorem Ipsum is simply dummy text of the printing and typesetting industry. Lorem Ipsum is simply dummy text of the printing and typesetting industry. Lorem Ipsum is simply dummy text of the printing and typesetting industry.</div>
  <div class="wordmark" style="left:6px;top:416px"><span class="name">MuroDeck</span><span class="place">NORDHAVEN</span></div>
  <span class="folio" style="bottom:50px">03</span>
</section>

<!-- Vision -->
<section class="page" style="left:1130px;top:24px">
  <div class="abs" style="left:0;top:0;width:205px;height:266px;background:linear-gradient(160deg,#d8dde0,#9aa9b6 45%,#5d6f86 75%,#c9cfd3)" role="img" aria-label="Two colleagues reviewing plans at a desk"></div>
  <div class="abs" style="left:205px;top:0;width:130px;height:266px;background:var(--teal)"></div>
  <div class="abs heading light" style="left:213px;top:18px;font-size:13.5px">VISION</div>
  <div class="abs lorem light" style="left:213px;top:50px;width:112px">Lorem Ipsum is simply dummy text of the printing and typesetting industry. Ut wisi enim ad minim veniam, quis nostrud exerci tation ullamcorper suscipit lobortis nisl ut aliquip ex ea commodo consequat. Duis autem vel eum iriure dolor in hendrerit in vulputate velit esse molestie consequat. Lorem Ipsum is simply dummy text of the printing and typesetting industry.</div>
  <div class="abs" style="left:27px;top:285px;font-size:5px;font-weight:700">LOREM IPSUM IS SIMPLY<br><span style="font-weight:400">Lorem Ipsum</span></div>
  <div class="abs lorem" style="left:27px;top:309px;width:120px">Lorem Ipsum is simply dummy text of the printing and typesetting industry. Ut wisi enim ad minim veniam, quis nostrud exerci tation ullamcorper suscipit lobortis nisl ut aliquip ex ea commodo consequat.</div>
  <div class="hex" style="left:212px;top:274px;width:88px;height:92px" role="img" aria-label="Stack of printed catalogues">
    <svg viewBox="0 0 100 100" preserveAspectRatio="none">
      <defs><linearGradient id="visionImg" x1="0" y1="0" x2="1" y2="1"><stop offset="0" stop-color="#e8e8e8"/><stop offset=".5" stop-color="#9aa3ab"/><stop offset="1" stop-color="#f2d35b"/></linearGradient></defs>
      <polygon points="50,0 100,25 100,75 50,100 0,75 0,25" fill="var(--teal)"/>
      <polygon points="50,5 96,28 96,72 50,95 4,72 4,28" fill="url(#visionImg)"/>
    </svg>
  </div>
  <div class="abs lorem" style="left:27px;top:367px;width:300px">Lorem Ipsum is simply dummy text of the printing and typesetting industry. Ut wisi enim ad minim veniam, quis nostrud exerci tation ullamcorper suscipit lobortis nisl ut aliquip ex ea commodo consequat.</div>
  <div class="wordmark" style="left:10px;top:416px"><span class="name">MuroDeck</span><span class="place">NORDHAVEN</span></div>
  <span class="folio" style="bottom:42px">04</span>
</section>

<!-- Mission -->
<section class="page" style="left:36px;top:516px">
  <div class="hex" style="left:20px;top:45px;width:148px;height:165px" role="img" aria-label="Hand signing a document with a pen">
    <svg viewBox="0 0 100 100" preserveAspectRatio="none">
      <defs><linearGradient id="missionImg" x1="0" y1="0" x2="1" y2="1"><stop offset="0" stop-color="#f4f4f4"/><stop offset=".6" stop-color="#e6cbb8"/><stop offset="1" stop-color="#cfd3d6"/></linearGradient></defs>
      <polygon points="50,0 100,25 100,75 50,100 0,75 0,25" fill="var(--teal)"/>
      <polygon points="50,6 95,28 95,72 50,94 5,72 5,28" fill="url(#missionImg)"/>
    </svg>
  </div>
  <div class="abs heading" style="left:186px;top:28px;font-size:13.5px">MISSION</div>
  <div class="abs lorem" style="left:186px;top:60px;width:125px">
    <p>Lorem Ipsum is simply dummy text of the printing and typesetting industry. Ut wisi enim ad minim veniam, quis nostrud exerci tation ullamcorper suscipit lobortis nisl ut aliquip ex ea commodo consequat. Duis autem vel eum iriure dolor in hendrerit in vulputate velit esse molestie consequat. Lorem Ipsum is simply dummy text of the printing and typesetting industry.</p>
    <p>Lorem Ipsum is simply dummy text of the printing and typesetting industry. Lorem Ipsum is simply dummy text of the printing and typesetting industry.</p>
  </div>
  <div class="abs lorem" style="left:20px;top:224px;width:300px">Lorem Ipsum is simply dummy text of the printing and typesetting industry. Lorem Ipsum is simply dummy text of the printing and typesetting industry. Lorem Ipsum is simply dummy text of the printing and typesetting industry.</div>
  <div class="abs" style="left:0;top:276px;width:335px;height:150px;background:var(--teal)"></div>
  <div class="abs" style="left:22px;top:295px;font-size:5px;font-weight:700;color:#fff">LOREM IPSUM IS SIMPLY<br><span style="font-weight:400">Lorem Ipsum</span></div>
  <div class="abs lorem light" style="left:22px;top:320px;width:120px">Lorem Ipsum is simply dummy text of the printing and typesetting industry. Ut wisi enim ad minim veniam, quis nostrud exerci tation ullamcorper suscipit lobortis nisl ut aliquip ex ea commodo consequat.</div>
  <div class="abs lorem light" style="left:172px;top:320px;width:148px">Lorem Ipsum is simply dummy text of the printing and typesetting industry. Ut wisi enim ad minim veniam, quis nostrud exerci tation ullamcorper suscipit lobortis nisl ut aliquip ex ea commodo consequat.</div>
  <div class="abs lorem light" style="left:22px;top:377px;width:290px">Lorem Ipsum is simply dummy text of the printing and typesetting industry. Ut wisi enim ad minim veniam, quis nostrud exerci tation ullamcorper suscipit lobortis nisl ut aliquip ex ea commodo consequat.</div>
  <div class="wordmark" style="left:10px;top:440px"><span class="name">MuroDeck</span><span class="place">NORDHAVEN</span></div>
  <span class="folio" style="bottom:28px">05</span>
</section>

<!-- Our best services -->
<section class="page" style="left:396px;top:516px">
  <div class="abs" style="left:185px;top:24px;width:150px;height:340px;background:var(--teal)"></div>
  <div class="abs heading" style="left:20px;top:22px;font-size:13.5px">OUR BEST SERVICES</div>
  <div class="abs lorem" style="left:20px;top:68px;width:145px">
    <p>Lorem Ipsum is simply dummy text of the printing and typesetting industry. Ut wisi enim ad minim veniam, quis nostrud exerci tation ullamcorper suscipit lobortis nisl ut aliquip ex ea commodo consequat.</p>
    <p>Lorem Ipsum is simply dummy text of the printing and typesetting industry.</p>
  </div>
  <div class="hex" style="left:198px;top:42px;width:124px;height:130px" role="img" aria-label="Cyan, magenta, yellow and black ink drops">
    <svg viewBox="0 0 100 100" preserveAspectRatio="none">
      <defs><linearGradient id="inkImg" x1="0" y1="0" x2="1" y2="1"><stop offset="0" stop-color="#f5f5f5"/><stop offset=".35" stop-color="#27b5e6"/><stop offset=".55" stop-color="#e5197c"/><stop offset=".75" stop-color="#f6de1d"/><stop offset="1" stop-color="#222"/></linearGradient></defs>
      <polygon points="50,0 100,25 100,75 50,100 0,75 0,25" fill="#fff"/>
      <polygon points="50,5 96,28 96,72 50,95 4,72 4,28" fill="url(#inkImg)"/>
    </svg>
  </div>
  <div class="hex" style="left:198px;top:200px;width:124px;height:135px" role="img" aria-label="Three-dimensional print lettering">
    <svg viewBox="0 0 100 100" preserveAspectRatio="none">
      <defs><linearGradient id="letterImg" x1="0" y1="0" x2="1" y2="1"><stop offset="0" stop-color="#ffffff"/><stop offset=".5" stop-color="#d6dadc"/><stop offset="1" stop-color="#7fcbe0"/></linearGradient></defs>
      <polygon points="50,0 100,25 100,75 50,100 0,75 0,25" fill="#fff"/>
      <polygon points="50,5 96,28 96,72 50,95 4,72 4,28" fill="url(#letterImg)"/>
    </svg>
  </div>
  <div class="num" style="top:170px">01</div><div class="num-text" style="top:171px">Lorem Ipsum is simply dummy text of the printing and typesetting industry.</div>
  <div class="num" style="top:199px">02</div><div class="num-text" style="top:200px">Lorem Ipsum is simply dummy text of the printing and typesetting industry.</div>
  <div class="num" style="top:227px">03</div><div class="num-text" style="top:228px">Lorem Ipsum is simply dummy text of the printing and typesetting industry.</div>
  <div class="num" style="top:256px">04</div><div class="num-text" style="top:257px">Lorem Ipsum is simply dummy text of the printing and typesetting industry.</div>
  <div class="num" style="top:284px">05</div><div class="num-text" style="top:285px">Lorem Ipsum is simply dummy text of the printing and typesetting industry.</div>
  <div class="num" style="top:313px">06</div><div class="num-text" style="top:314px">Lorem Ipsum is simply dummy text of the printing and typesetting industry.</div>
  <div class="num" style="top:341px">07</div><div class="num-text" style="top:342px">Lorem Ipsum is simply dummy text of the printing and typesetting industry.</div>
  <div class="wordmark" style="left:10px;top:440px"><span class="name">MuroDeck</span><span class="place">NORDHAVEN</span></div>
  <span class="folio" style="bottom:28px">06</span>
</section>

<!-- Our team -->
<section class="page" style="left:767px;top:516px">
  <div class="abs" style="left:0;top:26px;width:100px;height:366px;background:var(--teal)"></div>
  <div class="abs heading" style="left:137px;top:12px;font-size:15px">OUR TEAM</div>

  <div class="hex" style="left:55px;top:44px;width:66px;height:76px" role="img" aria-label="Portrait of team member"><svg viewBox="0 0 100 100" preserveAspectRatio="none"><polygon points="50,0 100,25 100,75 50,100 0,75 0,25" fill="#fff"/><polygon points="50,5 95,28 95,72 50,95 5,72 5,28" fill="#b9c7cc"/></svg></div>
  <div class="abs" style="left:137px;top:57px"><div class="member-name">EXAMPLE NAME</div><div class="member-role">Marketing Manager</div></div>
  <div class="abs lorem" style="left:137px;top:88px;width:170px;font-size:4px;line-height:6px">Lorem Ipsum is simply dummy text of the printing and typesetting industry. Lorem Ipsum is simply dummy text of the printing and typesetting industry.</div>

  <div class="hex" style="left:59px;top:134px;width:66px;height:76px" role="img" aria-label="Portrait of team member"><svg viewBox="0 0 100 100" preserveAspectRatio="none"><polygon points="50,0 100,25 100,75 50,100 0,75 0,25" fill="#fff"/><polygon points="50,5 95,28 95,72 50,95 5,72 5,28" fill="#9c8a7d"/></svg></div>
  <div class="abs" style="left:143px;top:146px"><div class="member-name">EXAMPLE NAME</div><div class="member-role">Marketing Manager</div></div>
  <div class="abs lorem" style="left:143px;top:177px;width:170px;font-size:4px;line-height:6px">Lorem Ipsum is simply dummy text of the printing and typesetting industry. Lorem Ipsum is simply dummy text of the printing and typesetting industry.</div>

  <div class="hex" style="left:59px;top:223px;width:66px;height:76px" role="img" aria-label="Portrait of team member"><svg viewBox="0 0 100 100" preserveAspectRatio="none"><polygon points="50,0 100,25 100,75 50,100 0,75 0,25" fill="#fff"/><polygon points="50,5 95,28 95,72 50,95 5,72 5,28" fill="#b07e6a"/></svg></div>
  <div class="abs" style="left:143px;top:235px"><div class="member-name">EXAMPLE NAME</div><div class="member-role">Senior Officer</div></div>
  <div class="abs lorem" style="left:143px;top:266px;width:170px;font-size:4px;line-height:6px">Lorem Ipsum is simply dummy text of the printing and typesetting industry. Lorem Ipsum is simply dummy text of the printing and typesetting industry.</div>

  <div class="hex" style="left:59px;top:312px;width:66px;height:76px" role="img" aria-label="Portrait of team member"><svg viewBox="0 0 100 100" preserveAspectRatio="none"><polygon points="50,0 100,25 100,75 50,100 0,75 0,25" fill="#fff"/><polygon points="50,5 95,28 95,72 50,95 5,72 5,28" fill="#8d8f93"/></svg></div>
  <div class="abs" style="left:143px;top:324px"><div class="member-name">EXAMPLE NAME</div><div class="member-role">Marketing Manager</div></div>
  <div class="abs lorem" style="left:143px;top:355px;width:170px;font-size:4px;line-height:6px">Lorem Ipsum is simply dummy text of the printing and typesetting industry. Lorem Ipsum is simply dummy text of the printing and typesetting industry.</div>

  <div class="wordmark" style="left:6px;top:440px"><span class="name">MuroDeck</span><span class="place">NORDHAVEN</span></div>
  <span class="folio" style="bottom:28px">07</span>
</section>

<!-- Contact -->
<section class="page" style="left:1130px;top:516px">
  <svg class="abs" style="left:0;top:0" width="335" height="474" viewBox="0 0 335 474" aria-hidden="true">
    <polygon points="0,105 0,150 335,400 335,330" fill="var(--teal)"/>
    <polygon points="240,30 335,30 335,125" fill="var(--teal)"/>
    <polygon points="200,250 335,250 335,370" fill="var(--teal)"/>
  </svg>
  <div class="wordmark" style="left:108px;top:54px"><span class="name" style="font-size:24px">MuroDeck</span><span class="place" style="font-size:6.5px">NORDHAVEN</span></div>
  <div class="hex" style="left:62px;top:108px;width:198px;height:220px" role="img" aria-label="Hand touching contact icons on a screen">
    <svg viewBox="0 0 100 100" preserveAspectRatio="none">
      <defs><linearGradient id="contactImg" x1="0" y1="0" x2="1" y2="1"><stop offset="0" stop-color="#f2f4f6"/><stop offset=".5" stop-color="#d3dde4"/><stop offset="1" stop-color="#eef1f3"/></linearGradient></defs>
      <polygon points="50,0 100,25 100,75 50,100 0,75 0,25" fill="#fff"/>
      <polygon points="50,3 97,27 97,73 50,97 3,73 3,27" fill="url(#contactImg)"/>
    </svg>
  </div>
  <div class="abs" style="left:126px;top:198px;font-size:14px;font-weight:400;color:#3d4a52">CONTACT US</div>
  <div class="abs heading" style="left:19px;top:342px;font-size:13.5px">CONTACT US</div>
  <div class="abs" style="left:20px;top:368px">
    <div class="contact-line"><svg viewBox="0 0 10 10"><path d="M5 0C3 0 1.5 1.5 1.5 3.5 1.5 6 5 10 5 10S8.5 6 8.5 3.5C8.5 1.5 7 0 5 0Zm0 5a1.5 1.5 0 1 1 0-3 1.5 1.5 0 0 1 0 3Z" fill="var(--teal)"/></svg><span>Your street address here.<br>Your city name. Your Country Name.</span></div>
    <div class="contact-line"><svg viewBox="0 0 10 10"><path d="M2 0.5 3.8 2.5 2.8 3.8C3.5 5.3 4.7 6.5 6.2 7.2L7.5 6.2 9.5 8 8.3 9.5C4 9.3.7 6 .5 1.7Z" fill="var(--teal)"/></svg><span>+ 04471 2208 15300<br>+ 04471 2208 15301</span></div>
    <div class="contact-line"><svg viewBox="0 0 10 10"><rect x="0.5" y="2" width="9" height="6.5" fill="var(--teal)"/><path d="M0.5 2 5 5.5 9.5 2" stroke="#fff" stroke-width=".8" fill="none"/></svg><span>hello@murodeck.example<br>info@murodeck.example</span></div>
    <div class="contact-line"><svg viewBox="0 0 10 10"><circle cx="5" cy="5" r="4.2" fill="none" stroke="var(--teal)" stroke-width="1"/><path d="M0.8 5h8.4M5 .8c-2.2 2.6-2.2 5.8 0 8.4M5 .8c2.2 2.6 2.2 5.8 0 8.4" stroke="var(--teal)" stroke-width=".8" fill="none"/></svg><span>www.murodeck.example</span></div>
  </div>
</section>

</div>
</body>
</html>
```